cover for CD- Single.

This design is for a CD cover. The design is at your disposal, using all of your creative talents.
Things to improve the photo: Cleaning the face, removing blemishes.
Design in black and white would be an option (Color would be another option). I reiterate it is up to your taste and criteria, any reform and art on the cover of Cd.
Name of the single: El Camino del Silencio
Artist Name: Marisol Duarte

Target Market(s)

Single Music

Industry/Entity Type

Music

Colors

Designer to choose colors to be used in the design.

Requirements
Must have
• style, elegance, professionalism, spontaneity
Nice to have
• I want it to be as professional as possible.
Should not have
• Spelling errors.

```html
<!DOCTYPE html>
<html lang="es">
<head>
<meta charset="utf-8">
<title>El Camino del Silencio — Marisol Duarte</title>
<link href="https://fonts.googleapis.com/css2?family=Josefin+Sans:wght@600;700&display=swap" rel="stylesheet">
<style>
  :root {
    --stage: #5b5b5b;
    --ink: #ffffff;
    --shade: #050505;
    --light-warm: #e9dca4;
    --skin: #d6b49c;
    --skin-deep: #a97f6a;
    --hair: #1e1719;
  }
  * { margin: 0; padding: 0; box-sizing: border-box; }
  html, body {
    width: 1200px;
    height: 554px;
    overflow: hidden;
    background: var(--stage);
  }
  .stage {
    width: 1200px;
    height: 554px;
    display: flex;
    align-items: center;
    justify-content: center;
  }
  .cover {
    position: relative;
    width: 530px;
    height: 530px;
    overflow: hidden;
    background: var(--shade);
    box-shadow: 0 6px 18px rgba(0,0,0,0.35);
  }
  .cover__photo {
    position: absolute;
    inset: 0;
    background: linear-gradient(105deg, var(--light-warm) 0%, var(--skin) 35%, var(--skin-deep) 68%, var(--hair) 92%);
  }
  .cover__fade {
    position: absolute;
    left: 0; right: 0; bottom: 0;
    height: 56%;
    background: linear-gradient(180deg, rgba(5,5,5,0) 0%, rgba(5,5,5,0.55) 45%, var(--shade) 85%);
  }
  .cover__type {
    position: absolute;
    left: 0; right: 0;
    top: 356px;
    text-align: center;
    color: var(--ink);
    font-family: "Josefin Sans", sans-serif;
    text-shadow: 0 2px 6px rgba(0,0,0,0.35);
  }
  .title__main {
    font-weight: 700;
    font-size: 64px;
    line-height: 1;
    letter-spacing: 0.02em;
  }
  .title__sub {
    margin-top: 2px;
    font-weight: 700;
    font-size: 28px;
    line-height: 1;
    letter-spacing: 0.42em;
    padding-left: 0.42em;
  }
  .artist {
    margin-top: 30px;
    font-weight: 600;
    font-size: 13px;
    letter-spacing: 0.42em;
    padding-left: 0.42em;
  }
</style>
</head>
<body>
  <main class="stage">
    <section class="cover">
      <div class="cover__photo" role="img" aria-label="Cover photograph of the singer in warm sunlight"></div>
      <div class="cover__fade"></div>
      <div class="cover__type">
        <h1 class="title__main">EL CAMINO</h1>
        <p class="title__sub">DEL SILENCIO</p>
        <p class="artist">MARISOL DUARTE</p>
      </div>
    </section>
  </main>
</body>
</html>
```